Maple Hollow Farm Business Card

Farm selling Nigerian Dwarf Goats, Bison, chickens, and miniature donkeys. Additionally we sell goats milk, goats milk soap and goat cheese, bison meat, bison heads, and bison skins, and chicken eggs.
Address 4125 Larkspur Road
Millbrook, KY 40999
Phone number 555-283-1947
Website: MapleHollowFarm@examplemail.com
I will upload my farm logo, cheese label, and soap label to give you ideas of my theme.
I want a really catchy card that people will remember.

```html
<!DOCTYPE html>
<html lang="en">
<head>
<meta charset="utf-8">
<title>Maple Hollow Farm Business Card</title>
<link href="https://fonts.googleapis.com/css2?family=Lato:wght@400;700;900&display=swap" rel="stylesheet">
<style>
  :root {
    --backdrop: #1c1c1c;
    --card: #2d2621;
    --card-edge: #3a312a;
    --gold: #e2b324;
    --silver: #cfcfcf;
    --white: #f0f0f0;
    --rope: #9a6a2c;
  }
  * { box-sizing: border-box; margin: 0; padding: 0; }
  html, body {
    width: 1200px; height: 900px; overflow: hidden;
    background: var(--backdrop);
    font-family: "Lato", Arial, sans-serif;
  }
  .canvas {
    width: 1200px; height: 900px;
    display: flex; flex-direction: column; align-items: center; justify-content: center;
    gap: 40px;
  }
  .card {
    position: relative;
    width: 700px; height: 400px;
    background: var(--card);
    border: 1px solid var(--card-edge);
    box-shadow: 0 10px 30px rgba(0,0,0,.5);
  }
  .brand {
    position: absolute;
    display: flex; flex-direction: column; align-items: center; gap: 10px;
  }
  .brand-mark {
    border-radius: 50%;
    border: 6px solid var(--rope);
  }
  .brand-name {
    color: var(--gold); font-weight: 900; letter-spacing: 1px;
    text-transform: uppercase; line-height: 1; white-space: nowrap;
  }

  /* front */
  .card-front .brand { top: 55px; left: 0; right: 0; }
  .card-front .brand-mark { width: 130px; height: 130px; }
  .card-front .brand-name { font-size: 30px; }
  .offerings {
    position: absolute; left: 0; right: 0; top: 270px;
    text-align: center; color: var(--gold); font-weight: 700; font-size: 19px; line-height: 1.5;
  }

  /* back */
  .card-back .brand { top: 40px; left: 60px; }
  .card-back .brand-mark { width: 120px; height: 120px; }
  .card-back .brand-name { font-size: 26px; }
  .person {
    position: absolute; top: 48px; right: 50px; text-align: right;
  }
  .person-name { color: var(--gold); font-weight: 900; font-size: 26px; letter-spacing: .5px; line-height: 1.1; }
  .person-role { color: var(--silver); font-weight: 700; font-size: 16px; letter-spacing: 1px; margin-top: 2px; }
  .address {
    position: absolute; right: 50px; top: 205px; text-align: right;
    color: var(--silver); font-weight: 700; font-size: 19px; line-height: 1.45;
  }
  .contacts {
    position: absolute; left: 55px; bottom: 34px;
    list-style: none; color: var(--white); font-weight: 700; font-size: 20px;
  }
  .contacts li { display: flex; align-items: center; gap: 10px; height: 34px; }
  .contacts svg { width: 20px; height: 20px; fill: var(--silver); flex: none; }
  .contacts .website { display: block; line-height: 34px; font-size: 22px; }
  .contacts .website span { color: var(--gold); }
</style>
</head>
<body>
<main class="canvas">
  <section class="card card-front">
    <div class="brand">
      <div class="brand-mark"></div>
      <div class="brand-name">Maple Hollow Farm</div>
    </div>
    <p class="offerings">Goats Milk, Goats Milk Soap &amp; Goat Cheese,<br>Bison Meat, Bison Heads, &amp; Bison Skins, &amp; Chicken Eggs</p>
  </section>

  <section class="card card-back">
    <div class="person">
      <div class="person-name">YOUR NAME</div>
      <div class="person-role">DESIGNATION</div>
    </div>
    <div class="brand">
      <div class="brand-mark"></div>
      <div class="brand-name">Maple Hollow Farm</div>
    </div>
    <p class="address">4125 Larkspur Road<br>Millbrook, KY 40999</p>
    <ul class="contacts">
      <li>
        <svg viewBox="0 0 24 24" aria-hidden="true"><path d="M3 7c0-2 3-3 9-3s9 1 9 3v2h-4V7.5C15.5 7 8.5 7 7 7.5V9H3zM6 11h12l2 8H4z"/></svg>
        555-283-1947
      </li>
      <li>
        <svg viewBox="0 0 24 24" aria-hidden="true"><path d="M2 5h20v14H2zM4 7v.5l8 5.5 8-5.5V7z"/></svg>
        MapleHollowFarm@examplemail.com
      </li>
      <li class="website">www.<span>MapleHollowFarm</span>.com</li>
    </ul>
  </section>
</main>
</body>
</html>
```